Need a fresh corporate identity for an existing Home Shopping Business in Thailand

We are one of the most active TV home shopping companies in Thailand. We need a fresh looking CI for our corporate, the colours of our corporate are Orange and Grey. We want our customers to see us as professional customer service who help them with their purchases.
The logo can be shown as a whole logo or either half logo but not less than half the logo.
Industry/Entity Type
Shopping
Requirements
Must have
- The logo should be shown at least half the logo or full logo.
Should not have
- The logo should not be shown less than half the logo.

```html
<!DOCTYPE html>
<html lang="en">
<head>
<meta charset="utf-8">
<title>Brightcart Stationery Set</title>
<link href="https://fonts.googleapis.com/css2?family=Open+Sans:wght@400;600;700&display=swap" rel="stylesheet">
<style>
  :root {
    --orange: #e2622a;
    --grey: #9d9d9f;
    --paper: #ffffff;
    --backdrop: #eeeeef;
    --ink: #4a4a4a;
    --ink-soft: #6d6d6d;
  }
  * { margin: 0; padding: 0; box-sizing: border-box; }
  html, body { width: 1200px; height: 937px; overflow: hidden; }
  body {
    background: var(--backdrop);
    font-family: "Open Sans", Arial, sans-serif;
    color: var(--ink);
    position: relative;
  }
  .sheet { position: absolute; background: var(--paper); overflow: hidden; }
  .sheet > svg.curve { position: absolute; inset: 0; width: 100%; height: 100%; }

  .brand { display: flex; align-items: center; gap: 6px; color: var(--orange); font-weight: 600; position: absolute; white-space: nowrap; }
  .brand .dot { border-radius: 50%; background: currentColor; flex: none; }

  /* Letterhead */
  .letterhead { left: 184px; top: 66px; width: 387px; height: 547px; }
  .letterhead .brand { left: 38px; top: 90px; font-size: 13px; }
  .letterhead .brand .dot { width: 12px; height: 12px; }
  .letter { position: absolute; left: 38px; top: 140px; width: 275px; font-size: 5.2px; line-height: 7.4px; color: var(--ink-soft); }
  .letter p { margin-bottom: 8px; }
  .letter .salutation { color: var(--ink); font-weight: 600; margin-bottom: 0; }
  .letter .gap { margin-bottom: 16px; }
  .signature { width: 28px; height: 12px; background: #e4e4e4; margin: 4px 0 6px; }
  .letter .signer { color: var(--ink); font-weight: 700; margin-bottom: 0; }
  .contact-block { position: absolute; right: 12px; bottom: 10px; text-align: right; color: #fff; font-size: 4.4px; line-height: 7.6px; font-weight: 600; }
  .contact-block .row { display: flex; justify-content: flex-end; align-items: center; gap: 3px; }
  .contact-block svg { width: 5px; height: 5px; fill: #fff; }

  /* Folder */
  .folder { left: 636px; top: 40px; width: 458px; height: 578px; }
  .folder .brand { left: 76px; top: 250px; font-size: 34px; gap: 12px; font-weight: 400; }
  .folder .brand .dot { width: 30px; height: 30px; }
  .web { position: absolute; color: #fff; letter-spacing: 2.6px; font-size: 12.5px; }
  .folder .web { right: 14px; bottom: 10px; }

  /* Business cards */
  .card-front { left: 45px; top: 658px; width: 176px; height: 100px; }
  .card-front .brand { left: 12px; top: 44px; font-size: 8.5px; gap: 3px; }
  .card-front .brand .dot { width: 7px; height: 7px; }
  .card-details { position: absolute; right: 6px; top: 9px; text-align: right; color: #fff; font-size: 4.2px; line-height: 6px; }
  .card-details .name { font-size: 5.4px; font-weight: 700; }
  .card-details .role { margin-bottom: 7px; }
  .card-details .numbers { margin-top: 6px; }
  .card-back { left: 45px; top: 785px; width: 176px; height: 100px; background: var(--orange); }
  .card-back .brand { color: #fff; left: 50%; top: 50%; transform: translate(-50%, -50%); font-size: 11px; font-weight: 400; flex-direction: column; gap: 4px; }
  .card-back .brand .dot { width: 26px; height: 26px; }

  /* Envelopes */
  .envelope-front { left: 265px; top: 672px; width: 432px; height: 209px; }
  .envelope-front .brand { left: 22px; top: 50px; font-size: 12px; gap: 5px; }
  .envelope-front .brand .dot { width: 10px; height: 10px; }
  .envelope-back { left: 737px; top: 672px; width: 433px; height: 209px; }
  .envelope-back .flap { position: absolute; left: 0; top: 0; width: 100%; height: 72px; background: var(--orange); border-radius: 0 0 30px 30px; }
  .envelope-back .web { left: 0; right: 0; top: 26px; text-align: center; font-size: 12px; }
</style>
</head>
<body>

<section class="sheet letterhead">
  <svg class="curve" viewBox="0 0 387 547" preserveAspectRatio="none" aria-hidden="true">
    <path d="M350,0 L366,0 C372,250 335,420 245,547 L232,547 C322,420 356,250 350,0 Z" fill="var(--grey)"/>
    <path d="M366,0 L387,0 L387,547 L245,547 C335,420 372,250 366,0 Z" fill="var(--orange)"/>
  </svg>
  <div class="brand"><span class="dot"></span>Brightcart</div>
  <div class="letter">
    <p>July 2, 2012</p>
    <p class="salutation">Dear CH,</p>
    <p>Sukhum Tower, Rama IV Rd., Bangkok</p>
    <p class="gap">Lorem ipsum is simply dummy text of the printing and typesetting industry. Lorem Ipsum has been the industry's standard dummy text ever since the 1500s, when an unknown printer took a galley of type and scrambled it to make a type specimen book. It has survived not only five centuries, but also the leap into electronic typesetting, remaining essentially unchanged. It was popularised in the 1960s with the release of Letraset sheets containing Lorem Ipsum passages, and more recently with desktop publishing software including versions of Lorem Ipsum.</p>
    <p class="gap">Lorem ipsum is simply dummy text of the printing and typesetting industry. Lorem Ipsum has been the industry's standard dummy text ever since the 1500s, when an unknown printer took a galley of type and scrambled it to make.</p>
    <p>Lorem ipsum is simply dummy text of the printing and typesetting industry. Lorem Ipsum has been the industry's standard dummy text ever since the 1500s, when an unknown printer took a galley of type and scrambled it to make a type specimen book. It has survived not only five centuries, but also the leap into electronic typesetting, remaining essentially unchanged. It was popularised in the 1960s with the release of Letraset sheets containing Lorem Ipsum passages, and more recently with desktop publishing software including versions of Lorem Ipsum.</p>
    <p>Best Regards,</p>
    <div class="signature" role="img" aria-label="Handwritten signature"></div>
    <p class="signer">Anan Wongsa</p>
    <p style="margin-bottom:0">Director</p>
    <p>Sukhum Tower, Rama IV Rd., Bangkok</p>
  </div>
  <div class="contact-block">
    <div class="row">1288 Rama IV Road</div>
    <div class="row">Klongtoey, Bangkok</div>
    <div class="row">02 345 6789 <svg viewBox="0 0 10 10"><path d="M2,1 L4,1 L5,3 L4,4 C4.5,5.5 5,6 6,6.5 L7,5.5 L9,6.5 L9,8.5 C5,9 1,5 2,1 Z"/></svg></div>
    <div class="row">02 345 6790 <svg viewBox="0 0 10 10"><rect x="3" y="1" width="4" height="8" rx="1"/></svg></div>
    <div class="row">02 345 6791 <svg viewBox="0 0 10 10"><rect x="1" y="4" width="8" height="5"/><rect x="3" y="1" width="4" height="3"/></svg></div>
    <div class="row">contact@brightcart.co <svg viewBox="0 0 10 10"><rect x="1" y="2" width="8" height="6"/></svg></div>
    <div class="row">www.brightcart.co <svg viewBox="0 0 10 10"><circle cx="5" cy="5" r="4"/></svg></div>
  </div>
</section>

<section class="sheet folder">
  <svg class="curve" viewBox="0 0 458 578" preserveAspectRatio="none" aria-hidden="true">
    <path d="M362,0 L386,0 C402,300 250,480 0,578 C225,470 380,290 362,0 Z" fill="var(--grey)"/>
    <path d="M386,0 L458,0 L458,578 L0,578 C250,480 402,300 386,0 Z" fill="var(--orange)"/>
  </svg>
  <div class="brand"><span class="dot"></span>Brightcart</div>
  <div class="web">www.brightcart-shop.com</div>
</section>

<section class="sheet card-front">
  <svg class="curve" viewBox="0 0 176 100" preserveAspectRatio="none" aria-hidden="true">
    <path d="M88,0 L98,0 C100,45 60,80 0,92 L0,86 C55,75 92,42 88,0 Z" fill="var(--grey)"/>
    <path d="M98,0 L176,0 L176,100 L0,100 L0,92 C60,80 100,45 98,0 Z" fill="var(--orange)"/>
  </svg>
  <div class="brand"><span class="dot"></span>Brightcart</div>
  <div class="card-details">
    <div class="name">NIRAN SATHIT</div>
    <div class="role">Managing Director</div>
    <div>1288 Rama IV Road</div>
    <div>Klongtoey, Bangkok</div>
    <div class="numbers">02 345 6789</div>
    <div>02 345 6790</div>
    <div>02 345 6791</div>
    <div>niran@brightcart.co</div>
    <div>www.brightcart.co</div>
  </div>
</section>

<section class="sheet card-back">
  <div class="brand"><span class="dot"></span>Brightcart</div>
</section>

<section class="sheet envelope-front">
  <svg class="curve" viewBox="0 0 432 209" preserveAspectRatio="none" aria-hidden="true">
    <path d="M390,0 L404,0 C410,90 360,160 265,209 L252,209 C348,160 396,90 390,0 Z" fill="var(--grey)"/>
    <path d="M404,0 L432,0 L432,209 L265,209 C360,160 410,90 404,0 Z" fill="var(--orange)"/>
  </svg>
  <div class="brand"><span class="dot"></span>Brightcart</div>
</section>

<section class="sheet envelope-back">
  <div class="flap"></div>
  <div class="web">www.brightcart-shop.com</div>
</section>

</body>
</html>
```